Summer Sunglass offer

Need a poster design for a spring / summer campaign. We are an opticians with good footfall. The design needs to be eye catching and aimed at 40 year old plus. The offer is Up to 50% off sunglass offer, t&c apply. (I have attached our last year campaign)
Also need a 2 sided A5 leaflet design (see attached)
I've uploaded a copy of our logo

A5 leaflet should read:

Grab a bargain on two great looks this summer Upto 50% off sunglasses
Look great and stay safe in the sun this summer

We want you to look great, feel fantastic and most of all stay safe in the sun this summer. That’s why we’re offering you 50% off prescription sunglasses with every complete pair of glasses you buy this summer or 25% off for prescription sunglasses with no other purchase.
Find you new summer looks from our gorgeous collection of frames in store. It matters to us that you look great in your new glasses as much as how well you see through them, so we’ll be on hand to help you find frames that suit you best.
What new looks will you go for? Smart or sassy? Formal or Fun? Whatever you’re in the mood for, you’ll find it in our collections this summer.
Call in today to find your new looks, and remember to bring your prescription if you don’t need an eye test.

Target Market(s)

40 + year old

Industry/Entity Type

Optician

Colors

Designer to choose colors to be used in the design.

Requirements
Must have
• Images, preferably a male and Female image

```html
<!DOCTYPE html>
<html lang="en">
<head>
<meta charset="utf-8">
<title>Summer Sunglass Offer – Larkfield Eyecare Centre</title>
<link href="https://fonts.googleapis.com/css2?family=Lato:wght@700;900&family=Oswald:wght@500;600&family=Barlow+Semi+Condensed:wght@300;400&family=Bebas+Neue&display=swap" rel="stylesheet">
<style>
  :root{
    --teal:#49a7b1;
    --blue:#2b5fae;
    --ink:#3a3a3a;
    --body:#222;
    --footer:#2a2a2b;
    --white:#fff;
  }
  *{margin:0;padding:0;box-sizing:border-box}
  html,body{width:847px;height:1200px;overflow:hidden;background:#fff}
  .poster{position:relative;width:847px;height:1200px;overflow:hidden;background:#fff;font-family:"Barlow Semi Condensed",sans-serif}
  .hero-photo{position:absolute;left:0;top:0;width:335px;height:937px;
    background:linear-gradient(180deg,#bcd9d8 0%,#7f9a9a 18%,#3b4240 45%,#2c2b27 70%,#1d2020 100%)}
  .header-bg{position:absolute;left:335px;top:0;width:512px;height:328px;
    background:linear-gradient(160deg,#e6e7e9 0%,#f4f4f5 45%,#fff 100%)}
  .headline{position:absolute;left:344px;top:40px;font-family:"Lato",sans-serif;font-weight:900;font-size:33px;line-height:42px}
  .headline .line-1{color:var(--blue);display:block;letter-spacing:1.5px}
  .headline .line-2{color:var(--ink);display:block;letter-spacing:-.2px}
  .offer-badge{position:absolute;left:438px;top:136px}
  .offer-title{position:absolute;left:440px;top:246px;font-family:"Oswald",sans-serif;font-weight:600;font-size:47px;color:var(--ink);letter-spacing:-.5px;transform:scaleX(.97);transform-origin:left}
  .copy{position:absolute;left:350px;top:327px;width:460px;font-size:22px;font-weight:300;line-height:29px;color:var(--body);text-align:justify;letter-spacing:.3px}
  .copy p{margin-bottom:20px}
  .cta-band{position:absolute;left:335px;top:794px;width:512px;height:143px;background:var(--teal)}
  .cta-band p{position:absolute;left:15px;top:20px;width:460px;color:var(--white);font-size:22px;font-weight:300;line-height:29px;text-align:justify;letter-spacing:.3px}
  .footer{position:absolute;left:0;top:937px;width:847px;height:263px;background:var(--footer)}
  .brand{position:absolute;left:56px;top:32px;display:flex;align-items:center;gap:14px}
  .brand-dot{width:46px;height:46px;border-radius:50%;background:var(--teal);flex:none}
  .brand-name{font-family:"Barlow Semi Condensed",sans-serif;font-weight:400;font-size:24px;letter-spacing:1px;color:var(--white);text-transform:uppercase;white-space:nowrap}
  .contact{position:absolute;left:42px;top:101px;list-style:none;color:#e8e8e8;font-size:22.5px;font-weight:300;line-height:27px}
  .contact li{display:flex;align-items:center;gap:10px}
  .contact svg{width:17px;height:17px;flex:none}
  .contact .web{color:var(--teal)}
  .divider{position:absolute;left:477px;top:19px;width:2px;height:200px;background:var(--teal)}
  .hours{position:absolute;left:576px;top:8px;color:#e8e8e8}
  .hours h2{font-family:"Oswald",sans-serif;font-weight:500;font-size:31px;color:var(--teal);letter-spacing:1px;margin-bottom:0;transform:scaleX(.88);transform-origin:left}
  .hours dl{font-size:21px;font-weight:300;line-height:26px}
  .hours dd{margin-bottom:10px}
</style>
</head>
<body>
<div class="poster">
  <div class="hero-photo" role="img" aria-label="Smiling couple embracing outdoors, both wearing sunglasses"></div>

  <div class="header-bg"></div>
  <h1 class="headline">
    <span class="line-1">GRAB A BARGAIN ON TWO</span>
    <span class="line-2">GREAT LOOKS THIS SUMMER</span>
  </h1>

  <svg class="offer-badge" width="265" height="112" viewBox="0 0 265 112" aria-label="Up to 50% off">
    <text x="0" y="108" font-family="Bebas Neue, sans-serif" font-size="150" fill="#49a7b1" letter-spacing="-4">50</text>
    <text transform="translate(130 96) rotate(-90)" font-family="Bebas Neue, sans-serif" font-size="36" fill="#3a3a3a" letter-spacing="1">UP TO</text>
    <text x="136" y="108" font-family="Bebas Neue, sans-serif" font-size="150" fill="#49a7b1">%</text>
    <rect x="238" y="2" width="24" height="106" rx="9" fill="#49a7b1"/>
    <text x="250" y="33" text-anchor="middle" font-family="Bebas Neue, sans-serif" font-size="30" fill="#fff">O</text>
    <text x="250" y="66" text-anchor="middle" font-family="Bebas Neue, sans-serif" font-size="30" fill="#fff">F</text>
    <text x="250" y="99" text-anchor="middle" font-family="Bebas Neue, sans-serif" font-size="30" fill="#fff">F</text>
  </svg>
  <div class="offer-title">Sunglass Offer</div>

  <div class="copy">
    <p>We want you to look great, feel fantastic and most of all stay safe in the sun this summer. That’s why we’re offering you 50% off prescription sunglasses with every complete pair of glasses you buy this summer or 25% off for prescription sunglasses with no other purchase.</p>
    <p>Find you new summer looks from our gorgeous collection of frames in store. It matters to us that you love how you look in your new glasses as much as how well you see through them, so we’ll be on hand to help you find frames that suit you best.</p>
    <p>What new looks will you go for? Smart or sassy? Formal or Fun? Whatever you’re in the mood for, you’ll find it in our collections this summer.</p>
  </div>

  <div class="cta-band">
    <p>Call in today to find your new looks, and remember to bring your prescription if you don’t need an eye test.</p>
  </div>

  <footer class="footer">
    <div class="brand">
      <span class="brand-dot"></span>
      <span class="brand-name">Larkfield Eyecare Centre</span>
    </div>
    <ul class="contact">
      <li><svg viewBox="0 0 16 16"><path d="M8 1a4.5 4.5 0 0 0-4.5 4.5C3.5 9 8 13 8 13s4.5-4 4.5-7.5A4.5 4.5 0 0 0 8 1z" fill="none" stroke="#49a7b1" stroke-width="1.4"/><circle cx="8" cy="5.5" r="1.6" fill="#49a7b1"/><path d="M2 15h12" stroke="#49a7b1" stroke-width="1.4"/></svg>142 Market St, Larkfield Kent LK4 2QT</li>
      <li><svg viewBox="0 0 16 16"><rect x="4" y="2" width="9" height="12" rx="2" fill="#e8e8e8"/><rect x="6" y="4" width="5" height="6" fill="#2a2a2b"/></svg>01632 960418</li>
      <li><svg viewBox="0 0 16 16"><rect x="1" y="3.5" width="14" height="9" fill="none" stroke="#e8e8e8" stroke-width="1.4"/><path d="M1 3.5l7 5 7-5" fill="none" stroke="#e8e8e8" stroke-width="1.4"/></svg>info@larkfieldeyecare.co.uk</li>
      <li class="web"><svg viewBox="0 0 16 16"><circle cx="8" cy="8" r="6.5" fill="none" stroke="#e8e8e8" stroke-width="1.4"/><path d="M1.5 8h13M8 1.5c3 3.5 3 9.5 0 13M8 1.5c-3 3.5-3 9.5 0 13" fill="none" stroke="#e8e8e8" stroke-width="1.1"/></svg>larkfieldeyecare.co.uk</li>
    </ul>
    <div class="divider"></div>
    <section class="hours">
      <h2>OPENING HOURS</h2>
      <dl>
        <dt>Monday - Thursday:</dt><dd>9:00am - 5:30pm</dd>
        <dt>Friday:</dt><dd>9:30am - 5:30pm</dd>
        <dt>Saturday:</dt><dd>9:00am - 4:00pm</dd>
      </dl>
    </section>
  </footer>
</div>
</body>
</html>
```